New Tech Support Service needs a website design

We need a web design for a new product we are developing that provides tech support to consumers for a small ongoing monthly fee. We are looking for a fresh, technology look and feel. We want the site to have a tech feel - yet not intimidating. Simple and welcoming. We are in need of an initial landing page, sign on page, and a product home page.

Thank you to everyone who submitted designs. It was a very difficult decision!

Tech

```html
<!DOCTYPE html>
<html lang="en">
<head>
<meta charset="utf-8">
<title>Helpora – Tech Support Landing Page</title>
<link href="https://fonts.googleapis.com/css2?family=Lato:wght@300;400;700;900&display=swap" rel="stylesheet">
<style>
:root{
  --blue:#4dc5f5;
  --blue-dark:#2fb2e8;
  --ink:#333333;
  --muted:#666666;
  --light:#f5f5f5;
  --white:#ffffff;
  --dark:#3a3a3a;
  --darker:#2e2e2e;
  --green:#8dc06a;
  --orange:#ff7d00;
  --line:#e2e2e2;
}
*{margin:0;padding:0;box-sizing:border-box}
html,body{width:1200px;height:3727px;overflow:hidden}
body{font-family:'Lato',Arial,sans-serif;color:var(--ink);background:var(--white);position:relative}
.abs{position:absolute}
section{position:absolute;left:0;width:1200px}

/* hero */
.hero{top:0;height:651px;background:linear-gradient(180deg,#0f1d2c 0%,#23384d 45%,#3b5770 100%);overflow:hidden}
.hero-photo{position:absolute;inset:0;background:radial-gradient(ellipse at 70% 45%,rgba(120,150,180,.35),transparent 60%),radial-gradient(ellipse at 20% 80%,rgba(90,120,150,.4),transparent 55%)}
.hero-device{position:absolute;left:273px;top:137px;width:286px;height:514px;background:linear-gradient(160deg,#2a2a2a 0%,#111 40%,#c9a48c 70%,#b48a72 100%);border-radius:40px 40px 0 0;opacity:.85}
.brand{position:absolute;left:127px;top:22px;font-weight:700;font-size:30px;color:var(--white);display:flex;align-items:center;gap:10px}
.brand .dot{width:10px;height:10px;border-radius:50%;background:var(--blue)}
.nav{position:absolute;left:601px;top:28px;display:flex;gap:0}
.nav a{font-size:11px;font-weight:700;color:var(--white);text-decoration:none;text-transform:uppercase;margin-right:40px;position:relative}
.nav a.active{color:var(--blue)}
.nav a.active::before{content:"";position:absolute;left:0;right:0;top:-28px;height:3px;background:var(--blue)}
.hero h1{position:absolute;left:529px;top:282px;font-size:33px;font-weight:300;color:var(--white)}
.hero h1 b{font-weight:700}
.hero p{position:absolute;left:529px;top:330px;width:610px;font-size:13px;line-height:1.35;color:var(--white)}
.btn{position:absolute;display:flex;align-items:center;justify-content:center;font-size:12px;font-weight:700;text-transform:uppercase;color:var(--white)}
.btn-outline{border:2px solid var(--white);border-radius:3px}
.btn-blue{background:var(--blue);border-radius:3px}
.available{position:absolute;left:529px;top:522px;font-size:13px;color:var(--white);display:flex;align-items:center;gap:14px}
.store{width:30px;height:30px;border-radius:50%;background:#555d66;display:flex;align-items:center;justify-content:center}
.arrow{position:absolute;width:42px;height:42px;border-radius:50%;display:flex;align-items:center;justify-content:center}
.dots{position:absolute;left:570px;top:619px;display:flex;gap:6px}
.dots i{width:13px;height:13px;border-radius:50%;border:2px solid var(--white)}
.dots i.on{background:var(--blue);border-color:var(--blue)}

/* section heads */
.head{position:absolute;left:0;width:1200px;text-align:center}
.head h2{font-size:28px;font-weight:700;color:var(--ink);line-height:1}
.head p{font-size:15px;color:var(--ink);margin-top:6px}

/* features */
.features{top:651px;height:472px;background:var(--light)}
.feature{position:absolute;width:240px;text-align:center}
.feature .icon{width:130px;height:130px;border-radius:50%;background:var(--blue);margin:0 auto;display:flex;align-items:center;justify-content:center}
.feature .icon.dark{background:var(--dark)}
.feature h3{font-size:12px;font-weight:700;text-transform:uppercase;margin-top:28px}
.feature h3.hl{color:var(--blue)}
.feature p,.shot p{font-size:10px;line-height:1.55;color:var(--muted);margin-top:10px;padding:0 16px}

/* gallery */
.gallery{top:1123px;height:467px;background:var(--white)}
.shot{position:absolute;top:131px;width:218px}
.shot .img{height:130px;background:radial-gradient(ellipse at 50% 55%,#9a9a9a,#3a3a3a 80%);border-radius:4px 4px 0 0}
.shot .img.blue{background:linear-gradient(160deg,#5aa9c9,#2a6f91)}
.shot .cap{height:32px;background:#3d4a52;color:var(--blue);font-size:11px;font-weight:700;text-transform:uppercase;display:flex;align-items:center;justify-content:center}
.shot p{text-align:center;margin-top:12px}

/* video */
.video{top:1590px;height:442px;background:linear-gradient(180deg,#6d8ea8 0%,#89a9c0 50%,#7a95ab 100%)}
.video h2{position:absolute;left:0;width:1200px;top:1800px;text-align:center}
.play{position:absolute;left:554px;top:129px;width:92px;height:57px;border:2px solid var(--white);border-radius:3px;display:flex;align-items:center;justify-content:center}
.video h2{top:213px;font-size:36px;font-weight:300;color:var(--white)}
.video h2 b{font-weight:700}
.video p{position:absolute;left:298px;top:270px;width:610px;font-size:13px;line-height:1.35;color:var(--white);font-weight:700}

/* pricing */
.pricing{top:2032px;height:571px;background:var(--white)}
.plan{position:absolute;background:#f8f8f8;border:1px solid var(--line);box-shadow:0 1px 4px rgba(0,0,0,.12);text-align:center}
.plan h4{font-size:12px;font-weight:400;color:#999;text-transform:uppercase;padding:24px 0 14px}
.plan .price{height:90px;display:flex;align-items:center;justify-content:center;color:var(--white);font-size:54px;font-weight:900}
.plan ul{list-style:none;padding-top:20px}
.plan li{font-size:13px;color:#999;line-height:34px}
.plan .buy{margin:12px auto 0;width:137px;height:38px;display:flex;align-items:center;justify-content:center;color:var(--white);font-size:11px;font-weight:700;text-transform:uppercase}
.plan.pro h4{color:var(--blue);font-size:15px;padding:20px 0 10px}
.plan.pro .price{height:95px;background:var(--blue);font-size:60px}
.plan.pro li{color:var(--blue);font-weight:700;line-height:32px}

/* testimonials */
.testimonials{top:2603px;height:313px;background:var(--light)}
.quote{position:absolute;left:537px;top:117px;width:290px;font-size:11px;line-height:1.4;color:var(--blue)}
.quote .by{text-align:right;margin-top:4px}
.pager{position:absolute;left:532px;top:275px;display:flex;gap:8px}
.pager i{width:40px;height:4px;background:#dde6ec}
.pager i.on{background:var(--blue)}

/* cta */
.cta{top:2916px;height:169px;background:var(--dark);text-align:center}
.cta h2{font-size:42px;font-weight:700;color:var(--white);padding-top:20px;letter-spacing:-1px}

/* contact */
.contact{top:3085px;height:554px;background:linear-gradient(135deg,#d7ddd2 0%,#e9e6dc 30%,#9cc9e8 50%,#e6e3d8 70%,#d9dcd3 100%)}
.contact-box{position:absolute;left:467px;top:87px;width:266px;height:373px;background:rgba(77,197,245,.85);border-radius:6px;text-align:center}
.contact-box h3{font-size:30px;font-weight:700;color:var(--white);padding-top:14px}
.field{position:absolute;left:22px;width:221px;height:30px;background:var(--white);border-radius:2px;font-size:11px;color:#aaa;display:flex;align-items:center;justify-content:center}
.field.area{height:120px;align-items:flex-start;padding-top:6px}
.send{position:absolute;left:60px;top:321px;width:154px;height:37px;background:var(--dark);border-radius:3px;color:var(--white);font-size:12px;display:flex;align-items:center;justify-content:center}

/* footer */
.footer{top:3639px;height:88px;background:var(--darker)}
.footer span{position:absolute;top:38px;font-size:10px;color:#888}
.footer b{color:var(--blue);font-weight:400}
</style>
</head>
<body>

<section class="hero">
  <div class="hero-photo" role="img" aria-label="Blurred city night photograph"></div>
  <div class="hero-device" role="img" aria-label="Hand holding a smartphone showing the app"></div>
  <div class="brand">Helpora<span class="dot"></span></div>
  <nav class="nav">
    <a class="active" href="#">Home</a><a href="#">Features</a><a href="#">Services</a><a href="#">Testimonials</a><a href="#">Download</a><a href="#">Contact</a>
  </nav>
  <div class="arrow" style="left:59px;top:302px;background:#2b5266">
    <svg width="12" height="14" viewBox="0 0 12 14"><path d="M9 1 3 7l6 6" fill="none" stroke="#4dc5f5" stroke-width="2"/></svg>
  </div>
  <div class="arrow" style="left:1099px;top:302px;background:var(--blue)">
    <svg width="12" height="14" viewBox="0 0 12 14"><path d="m3 1 6 6-6 6" fill="none" stroke="#fff" stroke-width="2"/></svg>
  </div>
  <h1>Simple, Beautiful <b>and Amazing</b></h1>
  <p>Lorem ipsum dolor sit amet, consectetur adipiscing elit. Nunc eget nunc vitae tellus luctus ullamcorper. Nam porttitor ullamcorper felis at convallis. Aenean ornare vestibulum nisi fringilla lacinia. Nullam pulvinar sollicitudin velit id laoreet. Quisque non rhoncus sem.</p>
  <div class="btn btn-outline" style="left:529px;top:420px;width:159px;height:50px">Download</div>
  <div class="btn btn-blue" style="left:723px;top:420px;width:156px;height:50px">Subscribe us</div>
  <div class="available">Available on :
    <span class="store"><svg width="14" height="14" viewBox="0 0 14 14"><circle cx="7" cy="8" r="5" fill="#4dc5f5"/></svg></span>
    <span class="store"><svg width="14" height="14" viewBox="0 0 14 14"><rect x="2" y="4" width="10" height="8" rx="2" fill="#fff"/></svg></span>
  </div>
  <div class="dots"><i class="on"></i><i></i><i></i></div>
</section>

<section class="features">
  <div class="head" style="top:48px"><h2>summarise the features</h2><p>summarise what your product is all about</p></div>
  <div class="feature" style="left:96px;top:141px">
    <div class="icon"><svg width="56" height="56" viewBox="0 0 56 56"><circle cx="28" cy="20" r="11" fill="#fff"/><path d="M8 50c0-12 9-18 20-18s20 6 20 18z" fill="#fff"/></svg></div>
    <h3>24/7 Support</h3>
    <p>Experts on call every hour of the day to fix your devices, answer questions and keep you connected.</p>
  </div>
  <div class="feature" style="left:352px;top:141px">
    <div class="icon"><svg width="40" height="62" viewBox="0 0 40 62"><rect x="3" y="3" width="34" height="56" rx="5" fill="none" stroke="#fff" stroke-width="4"/><rect x="9" y="10" width="22" height="38" fill="#fff"/></svg></div>
    <h3>Fresh Design</h3>
    <p>A clean and friendly interface that makes booking help simple, quick and pleasant for every visitor.</p>
  </div>
  <div class="feature" style="left:608px;top:141px">
    <div class="icon dark"><svg width="60" height="52" viewBox="0 0 60 52"><path d="M4 4h32v22H18l-8 7v-7H4z" fill="#fff"/><path d="M40 16h16v22h-6v7l-8-7H24v-8h16z" fill="#fff"/></svg></div>
    <h3 class="hl">Multipurpose</h3>
    <p>Help for phones, laptops, printers, home networks and smart gadgets, all covered under a single plan.</p>
  </div>
  <div class="feature" style="left:864px;top:141px">
    <div class="icon"><svg width="60" height="56" viewBox="0 0 60 56"><rect x="4" y="4" width="52" height="36" rx="3" fill="none" stroke="#fff" stroke-width="5"/><path d="M22 40h16l-8 10z" fill="#fff"/></svg></div>
    <h3>Easy to Customize</h3>
    <p>Pick the services you need, adjust your monthly package anytime and add devices whenever you like.</p>
  </div>
</section>

<section class="gallery">
  <div class="head" style="top:44px"><h2>show the product gallery</h2><p>summarise what your product is all about</p></div>
  <div class="shot" style="left:127px">
    <div class="img blue" role="img" aria-label="App screenshot one" style="display:flex;align-items:center;justify-content:center"><svg width="16" height="16" viewBox="0 0 16 16"><path d="M8 2v12M2 8h12" stroke="#fff" stroke-width="2"/></svg></div>
    <div class="cap">Screen shot #1</div>
    <p>Book a session in seconds and chat with a friendly technician who walks you through each step.</p>
  </div>
  <div class="shot" style="left:368px">
    <div class="img" role="img" aria-label="App screenshot two"></div>
    <div class="cap">Screen shot #2</div>
    <p>Track every open request, see progress live and get notified the moment your issue is solved.</p>
  </div>
  <div class="shot" style="left:611px">
    <div class="img" role="img" aria-label="App screenshot three"></div>
    <div class="cap">Screen shot #3</div>
    <p>Keep all your devices in one place with warranty dates, setup notes and helpful tips stored.</p>
  </div>
  <div class="shot" style="left:855px">
    <div class="img" role="img" aria-label="App screenshot four"></div>
    <div class="cap">Screen shot #4</div>
    <p>Manage your monthly plan, billing details and household members from a single simple screen.</p>
  </div>
</section>

<section class="video" role="img" aria-label="Blurred street photograph behind video promo">
  <div class="play"><svg width="24" height="26" viewBox="0 0 24 26"><path d="M3 2l19 11L3 24z" fill="#fff"/></svg></div>
  <h2>Watch the best Technology in <b>Action</b></h2>
  <p>Lorem ipsum dolor sit amet, consectetur adipiscing elit. Nunc eget nunc vitae tellus luctus ullamcorper. Nam porttitor ullamcorper felis at convallis. Aenean ornare vestibulum nisi fringilla lacinia. Nullam pulvinar sollicitudin velit id laoreet. Quisque non rhoncus sem.</p>
</section>

<section class="pricing">
  <div class="head" style="top:58px"><h2>choose your price</h2><p>summarise what your product is all about</p></div>
  <div class="plan" style="left:181px;top:164px;width:246px;height:338px">
    <h4>Basic Package</h4>
    <div class="price" style="background:var(--green)">20$</div>
    <ul><li>Features 1</li><li>Features 2</li><li>Features 3</li></ul>
    <div class="buy" style="background:var(--green)">Purchase</div>
  </div>
  <div class="plan pro" style="left:450px;top:149px;width:300px;height:370px">
    <h4>Professional Package</h4>
    <div class="price">25$</div>
    <ul><li>Features 1</li><li>Features 2</li><li>Features 3</li><li>Features 4</li></ul>
    <div class="buy" style="background:var(--blue);margin-top:14px">Purchase</div>
  </div>
  <div class="plan" style="left:773px;top:164px;width:245px;height:338px">
    <h4>Advanced Package</h4>
    <div class="price" style="background:var(--orange)">30$</div>
    <ul><li>Features 1</li><li>Features 2</li><li>Features 3</li></ul>
    <div class="buy" style="background:var(--orange)">Purchase</div>
  </div>
</section>

<section class="testimonials">
  <div class="head" style="top:37px"><h2>Testimonials</h2></div>
  <svg class="abs" style="left:390px;top:78px" width="120" height="130" viewBox="0 0 120 130">
    <path d="M60 2l56 32v62l-56 32L4 96V34z" fill="#fff"/>
    <path d="M60 12l48 27v52l-48 27-48-27V39z" fill="var(--blue)"/>
    <circle cx="60" cy="65" r="28" fill="none" stroke="#fff" stroke-width="4"/>
    <circle cx="60" cy="57" r="9" fill="#fff"/>
    <path d="M43 82c3-9 9-12 17-12s14 3 17 12z" fill="#fff"/>
  </svg>
  <div class="quote">
    Since joining, every little tech headache gets sorted within minutes. The team is patient, clear and always kind on the phone. Worth every cent of the monthly fee.
    <div class="by">Julia Marsh<br>Happy customer</div>
  </div>
  <div class="pager"><i class="on"></i><i></i><i></i></div>
</section>

<section class="cta">
  <h2>Do you Like this app?</h2>
  <div class="btn btn-blue" style="left:519px;top:92px;width:159px;height:47px;font-size:11px">Subscribe now</div>
</section>

<section class="contact">
  <div class="abs" style="inset:0" role="img" aria-label="Street map of the city around the office"></div>
  <div class="contact-box">
    <h3>Contact</h3>
    <div class="field" style="top:67px">Your name</div>
    <div class="field" style="top:107px">Your email</div>
    <div class="field" style="top:147px">Subject</div>
    <div class="field area" style="top:186px">Message</div>
    <div class="send">Send</div>
  </div>
</section>

<section class="footer">
  <span style="left:127px">Copyright © 2014 <b>Helpora</b> All Rights Reserved</span>
  <span style="left:939px">Terms of Service | Privacy Policy</span>
</section>

</body>
</html>
```